Personal Development Brand Needs a Workbook Cover Design

We need a clean and sleek cover design for our A4-Sized workbook called the "12-Week Horizon Logbook"

There's around 90 pages in the workbook, if that matters for the spine.

Necessary Elements on the Front Cover:

- Logo
- Title: Peak Lantern Horizon Logbook
- Subtitle: A Simple Workbook to Track Your Transformation
- Author Name: Dale Wrenfold

Elements on Back Cover:

- The Peak Lantern Creed

```html
<!DOCTYPE html>
<html lang="en">
<head>
<meta charset="utf-8">
<title>Peak Lantern Horizon Logbook — Cover</title>
<link rel="stylesheet" href="https://fonts.googleapis.com/css2?family=Oswald:wght@600;700&family=Montserrat:wght@600&display=swap">
<style>
  :root {
    --backdrop: #595959;
    --cover-navy: #151932;
    --cover-deep: #0f1226;
    --glow-blue: #1d3d78;
    --wire-cyan: #2fc3d6;
    --title-white: #f4f4f4;
    --title-red: #d9161c;
    --subtitle-grey: #e6e6e6;
  }
  * { margin: 0; padding: 0; box-sizing: border-box; }
  html, body {
    width: 1200px;
    height: 947px;
    overflow: hidden;
    background: var(--backdrop);
  }
  .stage {
    position: relative;
    width: 1200px;
    height: 947px;
  }
  .cover {
    position: absolute;
    left: 310px;
    top: 64px;
    width: 580px;
    height: 820px;
    background:
      radial-gradient(ellipse 60% 45% at 20% 72%, var(--glow-blue) 0%, transparent 75%),
      linear-gradient(180deg, var(--cover-navy) 0%, var(--cover-deep) 100%);
    overflow: hidden;
    box-shadow: 0 18px 40px rgba(0,0,0,0.35);
  }
  .figure-art {
    position: absolute;
    left: 0;
    top: 0;
    width: 170px;
    height: 700px;
    background: linear-gradient(90deg, rgba(47,195,214,0.55) 0%, rgba(47,195,214,0.28) 55%, rgba(47,195,214,0) 100%);
  }
  .title {
    position: absolute;
    right: 64px;
    top: 92px;
    text-align: right;
    font-family: "Oswald", sans-serif;
    font-weight: 700;
    text-transform: uppercase;
    line-height: 0.95;
  }
  .title-brand {
    display: block;
    color: var(--title-white);
    font-size: 78px;
    letter-spacing: 1px;
  }
  .title-middle {
    display: block;
    color: var(--title-red);
    font-size: 60px;
    letter-spacing: 1px;
  }
  .title-last {
    display: block;
    color: var(--title-red);
    font-size: 112px;
    letter-spacing: 1px;
    line-height: 0.92;
  }
  .subtitle {
    position: absolute;
    left: 120px;
    right: 60px;
    top: 440px;
    text-align: center;
    color: var(--subtitle-grey);
    font-family: "Oswald", sans-serif;
    font-weight: 600;
    font-size: 25px;
    line-height: 1.35;
    letter-spacing: 1px;
    text-transform: uppercase;
  }
  .author {
    position: absolute;
    left: 0;
    right: 0;
    bottom: 56px;
    text-align: center;
    color: var(--title-white);
    font-family: "Montserrat", sans-serif;
    font-weight: 600;
    font-size: 32px;
    letter-spacing: 0.42em;
    text-transform: uppercase;
  }
</style>
</head>
<body>
  <main class="stage">
    <section class="cover">
      <div class="figure-art" role="img" aria-label="Wireframe network illustration of a standing human figure in cyan lines"></div>
      <h1 class="title">
        <span class="title-brand">Peak Lantern</span>
        <span class="title-middle">Horizon</span>
        <span class="title-last">Logbook</span>
      </h1>
      <p class="subtitle">A Simple Workbook to Track<br>Your Transformation</p>
      <p class="author">Dale Wrenfold</p>
    </section>
  </main>
</body>
</html>
```